Looking for potential sellers

We help people buy and sell homes and are currently looking for potential home sellers. We offer low commissions, are the Local Colorado Springs and Falcon Experts, homes selling fast and at top dollar, Free expert pricing opinions and Consultations, over 9 years of experience, top rated Realtors creative and aggressive marketing strategies. Don't just tour the town, ROAM Kestrelby. phone number 555-013-8842 web roamkestrelby.example

```html
<!DOCTYPE html>
<html lang="en">
<head>
<meta charset="utf-8">
<title>Looking to Sell Your Home? – Ridgeline Homes Postcard</title>
<link rel="stylesheet" href="https://fonts.googleapis.com/css2?family=Poppins:wght@400;500;600;700;800&display=swap">
<style>
  :root{
    --page:#e9e7e2;
    --olive:#a4a66a;
    --olive-light:#b6b87c;
    --ink:#262b33;
    --white:#ffffff;
    --taupe:#8f857c;
    --taupe-dark:#6f665f;
    --paper:#fbfbfa;
    --rule:#d9d9d6;
    --scene-top:#5e5058;
    --scene-bottom:#2f3a33;
  }
  *{box-sizing:border-box;margin:0;padding:0}
  html,body{width:1200px;height:960px;overflow:hidden}
  body{background:var(--page);font-family:'Poppins',sans-serif;position:relative}

  .card{position:absolute;overflow:hidden;box-shadow:0 14px 30px rgba(40,35,30,.18)}

  /* ---------- Front ---------- */
  .card-front{left:40px;top:40px;width:720px;height:480px;background:var(--ink)}
  .intro-panel{position:absolute;left:0;top:0;width:390px;height:280px;
    background:linear-gradient(135deg,var(--olive-light),var(--olive));padding:22px 30px 0 34px;color:var(--white)}
  .brand{display:flex;align-items:center;gap:8px;font-weight:500;font-size:17px;letter-spacing:.5px;margin-left:40px;white-space:nowrap}
  .brand-mark{width:10px;height:10px;border:1.5px solid var(--white);flex:none}
  .headline{margin-top:22px;font-weight:800;font-size:30px;line-height:1.12}
  .headline-rule{width:230px;height:2px;background:var(--white);margin:12px 0 10px}
  .intro-copy{font-size:10.5px;line-height:1.5;font-weight:400;max-width:320px}

  .scenery{position:absolute;left:390px;top:0;width:330px;height:300px;
    background:linear-gradient(180deg,var(--scene-top),var(--scene-bottom))}
  .site-url{position:absolute;right:18px;top:14px;color:var(--white);font-size:12px;font-weight:500}

  .features{position:absolute;left:0;top:296px;width:720px;display:flex;padding:0 26px}
  .feature{flex:1;display:flex;align-items:center;gap:12px}
  .feature-icon{width:46px;height:46px;background:var(--olive);display:flex;align-items:center;justify-content:center;flex:none}
  .feature-title{font-weight:700;font-size:13px;line-height:1.2;color:var(--white);text-transform:uppercase}
  .feature-title span{display:block;color:var(--olive)}

  .details{position:absolute;left:0;top:378px;width:720px;display:flex;padding:0 26px}
  .detail{flex:1;font-size:12.5px;line-height:1.45;color:var(--white);padding-left:14px;border-left:1.5px solid var(--white)}
  .detail:first-child{border-left:none;padding-left:0}
  .detail strong{display:block;font-weight:700;font-size:15px;letter-spacing:.5px}
  .bottom-stripe{position:absolute;left:0;bottom:0;width:100%;height:18px;background:var(--olive)}

  /* ---------- Back ---------- */
  .card-back{left:680px;top:580px;width:480px;height:320px;background:var(--paper)}
  .back-panel{position:absolute;left:0;top:0;width:290px;height:100%;
    background:linear-gradient(160deg,var(--taupe),var(--taupe-dark));color:var(--white);padding:18px 20px}
  .back-heading{font-weight:800;font-size:22px}
  .back-copy{font-size:8px;line-height:1.5;margin-top:6px;max-width:250px}
  .portrait{position:absolute;left:20px;bottom:0;width:120px;height:150px;background:#5f5a58}
  .back-contact{position:absolute;left:150px;bottom:26px;width:126px;font-size:9px;line-height:1.4}
  .back-contact .brand{margin:0 0 8px;font-size:11.5px;letter-spacing:.2px;gap:6px}
  .back-contact .brand-mark{width:8px;height:8px}
  .back-contact strong{display:block;font-weight:700;font-size:13px}
  .stamp-box{position:absolute;right:22px;top:22px;width:58px;height:68px;border:1.5px solid var(--rule)}
  .address-lines{position:absolute;left:318px;top:150px;width:140px}
  .address-lines div{height:1.5px;background:var(--rule);margin-bottom:26px}
</style>
</head>
<body>

<section class="card card-front">
  <div class="intro-panel">
    <div class="brand"><span class="brand-mark"></span>Ridgeline Homes</div>
    <h1 class="headline">Looking to Sell<br>Your Home?</h1>
    <div class="headline-rule"></div>
    <p class="intro-copy">There's never been a better time to sell your home in Colorado Springs! With home values rising almost 10% in the last year alone, and predicted to jump another 3.7% within the year, it truly is a seller's market!</p>
  </div>

  <div class="scenery" role="img" aria-label="Photograph of a mountain lake among forested peaks at sunset">
    <span class="site-url">roamkestrelby.example</span>
  </div>

  <div class="features">
    <div class="feature">
      <div class="feature-icon">
        <svg width="26" height="26" viewBox="0 0 26 26" fill="none" stroke="#fff" stroke-width="2"><line x1="5" y1="21" x2="21" y2="5"/><circle cx="7" cy="7" r="3"/><circle cx="19" cy="19" r="3"/></svg>
      </div>
      <div class="feature-title">Low<span>Commissions</span></div>
    </div>
    <div class="feature">
      <div class="feature-icon">
        <svg width="26" height="26" viewBox="0 0 26 26" fill="none" stroke="#fff" stroke-width="2"><polyline points="3,20 10,13 14,17 23,7"/><polyline points="17,7 23,7 23,13"/></svg>
      </div>
      <div class="feature-title">Fast Selling and<span>at Top Dollar</span></div>
    </div>
    <div class="feature">
      <div class="feature-icon">
        <svg width="26" height="26" viewBox="0 0 26 26" fill="none" stroke="#fff" stroke-width="2"><path d="M3 5h14v10H9l-4 4v-4H3z"/><path d="M19 10h4v9h-2v3l-3-3h-6v-2"/></svg>
      </div>
      <div class="feature-title">Free Expert Pricing<span>Consultations</span></div>
    </div>
  </div>

  <div class="details">
    <p class="detail">Over 9 years of experience,<br>top rated Realtors</p>
    <p class="detail">Ready to make a change?<br>Contact us to sell your property today!</p>
    <p class="detail">Get in touch with us<strong>555-013-8842</strong></p>
  </div>
  <div class="bottom-stripe"></div>
</section>

<section class="card card-back">
  <div class="back-panel">
    <h2 class="back-heading">It's Time.</h2>
    <p class="back-copy">Whether you are moving up, scaling down or starting fresh, our team makes selling simple, quick and rewarding. Call today and see what your home is worth.</p>
    <div class="portrait" role="img" aria-label="Portrait photograph of the realtor in a suit"></div>
    <div class="back-contact">
      <div class="brand"><span class="brand-mark"></span>Ridgeline Homes</div>
      Get in touch with us
      <strong>555-013-8842</strong>
      roamkestrelby.example
    </div>
  </div>
  <div class="stamp-box"></div>
  <div class="address-lines"><div></div><div></div><div></div><div></div></div>
</section>

</body>
</html>
```